2 page flyer for a turf supply company. MERIDELL TURF SOLUTIONS

Design a marketing flyer to be distributed to landscaping contractors, councils, and private users.
I have attached a FileCrate link that holds the logo files, copy, and brand guidelines and images.
I am wanting the brochure to be 2 pages, which can be sent as a pdf or printed double-sided. I would like a modern, professional look using the colours from the brand guidelines. We are designing a new website so this brochure will be found on the website as well as sent to clients. I have uploaded the copy, a logo, and brand guidelines. The link to more photos and logos are found on the FileCrate link below.
https://www.filecrate-share.example/scl/fo/qwk83zmtlpdnv5b2hxcrt/h?rlkey=914vbnkstpqwe7yz2mcx8lf4d&dl=0
Here is the link to the current website. https://meridellgroup.com.au/
New one coming.

Target Market(s)

The decision makers at councils, landscape businesses and land developers

Industry/Entity Type

landscaping companies and councils

Font styles to use
Sans Serif

Requirements
Must have
• must be eye catching and easy to read
Nice to have
• Bold headings

```html
<!DOCTYPE html>
<html lang="en">
<head>
<meta charset="utf-8">
<title>Meridell Turf Solutions – Two-Page Flyer</title>
<link href="https://fonts.googleapis.com/css2?family=Poppins:ital,wght@0,400;0,500;0,600;0,700;0,800;1,400&display=swap" rel="stylesheet">
<style>
:root{
  --stage:#838383;
  --navy:#17507a;
  --navy-deep:#123d60;
  --green:#8cc63f;
  --green-mid:#6fb53a;
  --teal:#7bbaa8;
  --cream:#f3f6e7;
  --ink:#2e2e2e;
  --white:#ffffff;
}
*{margin:0;padding:0;box-sizing:border-box}
html,body{width:1200px;height:799px;overflow:hidden;background:var(--stage)}
body{position:relative;font-family:"Poppins",sans-serif;color:var(--ink)}
.side-label{position:absolute;top:40px;width:521px;text-align:center;color:var(--white);font-weight:700;font-size:25px;letter-spacing:1px}
.page{position:absolute;top:80px;width:521px;height:673px;overflow:hidden;background:linear-gradient(180deg,#fff 0%,var(--cream) 40%,#eef3dc 100%)}
.page--front{left:70px}
.page--back{left:626px}
.page svg.backdrop{position:absolute;left:0;top:0;width:521px;height:673px}
.abs{position:absolute}

.brand{position:absolute;display:flex;align-items:center;gap:10px}
.brand__dot{width:46px;height:46px;border-radius:50%;background:var(--navy)}
.brand__name{font-weight:700;color:var(--navy);font-size:15px;line-height:1.15;letter-spacing:.5px}

.hero-intro{left:35px;top:101px;color:var(--white);font-weight:700;font-size:16.5px;line-height:17px}
.hero-title{left:34px;top:135px;color:var(--white);font-weight:800;font-size:25px;line-height:25px}
.hero-welcome{left:35px;top:190px;color:var(--white);font-size:7.6px;line-height:10px;width:220px}
.trust-pill{left:30px;top:223px;width:295px;height:33px;border-radius:8px;background:var(--navy-deep);display:flex;align-items:center;gap:8px;padding-left:8px}
.trust-pill p{color:var(--white);font-size:7.8px;line-height:10.5px}
.trust-pill strong{color:var(--green);font-weight:600}

.feature{position:absolute}
.feature__head{display:flex;align-items:center;gap:7px}
.badge{width:35px;height:35px;flex:none}
.feature h3{font-weight:700;font-size:11px;line-height:14px;color:var(--ink);text-transform:uppercase}
.feature p{font-size:7.3px;line-height:9px;margin-top:10px;color:#333}
.feature p .cta{color:var(--navy);font-weight:700;font-style:italic}

.footer-contact{position:absolute;left:0;top:648px;width:521px;height:18px}
.footer-contact .label{position:absolute;left:32px;top:0;color:var(--white);font-weight:600;font-size:14.5px;letter-spacing:.5px}
.contact-item{position:absolute;top:3px;display:flex;align-items:center;gap:3px;color:var(--white);font-size:9.6px;font-weight:500}
.contact-item svg{width:8px;height:8px}

.varieties-pill{left:26px;top:88px;width:295px;height:26px;border-radius:7px;background:var(--navy-deep);color:var(--white);font-weight:700;font-size:12.6px;line-height:26px;padding-left:22px}
.variety{position:absolute;color:var(--white)}
.variety h4{font-weight:700;font-size:11.2px;line-height:14px;display:flex;gap:6px;align-items:flex-start}
.variety h4 svg{width:11px;height:11px;flex:none;margin-top:1px}
.variety p{font-size:7.5px;line-height:9px;margin-top:2px;color:#eef6e6}

.services-title{left:41px;top:470px;font-weight:700;font-size:14.8px;line-height:17px;color:var(--navy)}
.services-title .accent{color:var(--green-mid)}
.services-list{left:41px;top:506px;list-style:none;width:215px}
.services-list li{display:flex;gap:5px;font-size:9px;line-height:13.3px;font-weight:500;color:var(--ink)}
.services-list li svg{width:8px;height:8px;flex:none;margin-top:2.5px}

.testimonials-title{left:263px;top:395px;font-weight:700;font-size:14.8px;color:var(--navy)}
.testimonial{position:absolute;left:265px;width:232px;height:48px;border:1px solid #9bbf7a;border-radius:8px}
.testimonial .quote{position:absolute;left:15px;top:-10px;color:var(--green-mid);font-weight:800;font-size:17px;background:#f1f5e3;padding:0 2px;line-height:16px}
.testimonial p{position:absolute;left:15px;top:8px;width:205px;font-style:italic;font-size:7.4px;line-height:9px;color:#333}
.testimonial .author{position:absolute;left:116px;bottom:-6px;width:101px;height:12px;border-radius:6px;background:var(--navy-deep);color:var(--white);font-size:7.3px;font-weight:600;text-align:center;line-height:12px}
</style>
</head>
<body>

<div class="side-label" style="left:70px">FRONT</div>
<div class="side-label" style="left:626px">BACK</div>

<!-- ===== Front page ===== -->
<section class="page page--front">
  <svg class="backdrop" viewBox="0 0 521 673" aria-hidden="false">
    <defs>
      <linearGradient id="heroBand" x1="0" y1="0" x2="1" y2="0">
        <stop offset="0" stop-color="#7dbe3e"/>
        <stop offset="0.55" stop-color="#2a7068"/>
        <stop offset="1" stop-color="#17507a"/>
      </linearGradient>
      <linearGradient id="ringGreen" x1="0" y1="0" x2="0" y2="1">
        <stop offset="0" stop-color="#8cc63f"/>
        <stop offset="1" stop-color="#3f8f57"/>
      </linearGradient>
      <linearGradient id="parkPhoto" x1="0" y1="0" x2="0" y2="1">
        <stop offset="0" stop-color="#3f8fd8"/>
        <stop offset="0.45" stop-color="#9cc4e6"/>
        <stop offset="0.55" stop-color="#5c8a35"/>
        <stop offset="1" stop-color="#6aa73a"/>
      </linearGradient>
      <linearGradient id="fieldPhoto" x1="0" y1="0" x2="0" y2="1">
        <stop offset="0" stop-color="#5b8fc9"/>
        <stop offset="0.35" stop-color="#3d5f33"/>
        <stop offset="0.6" stop-color="#7fa843"/>
        <stop offset="1" stop-color="#6e6e62"/>
      </linearGradient>
      <linearGradient id="grassStrip" x1="0" y1="0" x2="0" y2="1">
        <stop offset="0" stop-color="#7fc447"/>
        <stop offset="0.7" stop-color="#3f8a2a"/>
        <stop offset="1" stop-color="#3a2c22"/>
      </linearGradient>
      <linearGradient id="lawnPhoto" x1="0" y1="0" x2="0" y2="1">
        <stop offset="0" stop-color="#9cc0d8"/>
        <stop offset="0.35" stop-color="#5b8a48"/>
        <stop offset="1" stop-color="#5fa43a"/>
      </linearGradient>
    </defs>
    <!-- hero band -->
    <path d="M0,90 C80,78 190,82 250,110 L400,222 C250,212 100,225 0,265 Z" fill="url(#heroBand)"/>
    <path d="M10,92 C90,68 200,70 265,95 L255,98 C190,78 90,78 10,95 Z" fill="#8cc63f"/>
    <!-- large photo with ring -->
    <circle cx="384" cy="88" r="152" fill="url(#ringGreen)"/>
    <circle cx="390" cy="86" r="140" fill="url(#parkPhoto)" role="img" aria-label="Photo: park pathway through green turf under blue sky with trees"/>
    <!-- small photo with ring -->
    <circle cx="475" cy="208" r="63" fill="#8cc63f"/>
    <circle cx="478" cy="209" r="57" fill="url(#fieldPhoto)" role="img" aria-label="Photo: open sports field with tree line"/>
    <!-- grass strip -->
    <rect x="290" y="585" width="175" height="60" rx="6" fill="url(#grassStrip)" role="img" aria-label="Image: cut-away strip of turf showing grass blades and soil"/>
    <!-- footer -->
    <path d="M0,673 L0,615 C150,598 360,612 521,588 L521,673 Z" fill="#17507a"/>
    <path d="M150,608 C280,600 400,606 521,584 L521,590 C400,612 280,606 150,611 Z" fill="#8cc63f"/>
    <circle cx="80" cy="712" r="110" fill="#7bbaa8"/>
    <circle cx="76" cy="714" r="103" fill="url(#lawnPhoto)" role="img" aria-label="Photo: green lawn in front of a building"/>
  </svg>

  <div class="brand" style="left:30px;top:20px">
    <span class="brand__dot"></span>
    <span class="brand__name">MERIDELL<br>TURF SOLUTIONS</span>
  </div>

  <p class="abs hero-intro">Discover the<br>Green Difference with</p>
  <h1 class="abs hero-title">MERIDELL TURF<br>SOLUTIONS</h1>
  <p class="abs hero-welcome">Welcome to Meridell Turf Solutions (MTS) – your gateway to a vibrant, green landscape!</p>

  <div class="abs trust-pill">
    <svg width="20" height="20" viewBox="0 0 20 20"><circle cx="10" cy="10" r="8" fill="none" stroke="#fff" stroke-width="1.2"/><path d="M6 10l3 3 5-6" fill="none" stroke="#8cc63f" stroke-width="1.5"/></svg>
    <p>With over two decades of expertise in the turf industry,<br><strong>we are your trusted partner for superior turf solutions.</strong></p>
  </div>

  <article class="feature" style="left:32px;top:272px;width:228px">
    <div class="feature__head">
      <svg class="badge" viewBox="0 0 36 36"><circle cx="18" cy="18" r="17" fill="#8cc63f"/><path d="M10 25h16M13 25c0-6 2-9 2-12M18 25V11M23 25c0-6-2-9-2-12" stroke="#fff" stroke-width="1.4" fill="none"/></svg>
      <h3>Premium turf products<br>across NSW</h3>
    </div>
    <p>Over the years, our commitment to excellence has propelled us to supply premium turf products across New South Wales. Our diverse clientele includes professional sporting fields, Council parks, housing estate playing fields, public parks and gardens, as well as domestic gardens and landscaping projects</p>
  </article>

  <article class="feature" style="left:274px;top:272px;width:232px">
    <div class="feature__head">
      <svg class="badge" viewBox="0 0 36 36"><circle cx="18" cy="18" r="17" fill="#8cc63f"/><circle cx="18" cy="14" r="5" stroke="#fff" stroke-width="1.4" fill="none"/><path d="M9 24h8l4-3h6" stroke="#fff" stroke-width="1.4" fill="none"/></svg>
      <h3>Tailored solutions<br>for every space</h3>
    </div>
    <p>Meridell Turf Solutions offers a range of turf varieties. Our commitment to quality extends to providing thick-cut turf, available in convenient maxi rolls or standard turf rolls. No matter the size of your project, we've got the perfect solution to bring your vision to life.</p>
  </article>

  <article class="feature" style="left:32px;top:378px;width:228px">
    <div class="feature__head">
      <svg class="badge" viewBox="0 0 36 36"><circle cx="18" cy="18" r="17" fill="#8cc63f"/><path d="M11 25V18M16 25V14M21 25V16M26 25V11" stroke="#fff" stroke-width="1.6"/></svg>
      <h3>The Meridell Advantage</h3>
    </div>
    <p>What sets our turf apart is its origin – meticulously grown in the rich alluvial soils of the fertile Riverbend Lowlands, ensuring the cultivation of top-tier turf characterised by quality, resilience, and durability. Spanning approximately 300 acres along the Wollan River, Meridell Turf Solutions boasts one of the largest turf farm land owners in the district. Our expansive land, coupled with full irrigation capabilities, positions MTS as a reliable source of drought-resistant turf supplies</p>
  </article>

  <article class="feature" style="left:274px;top:378px;width:232px">
    <div class="feature__head">
      <svg class="badge" viewBox="0 0 36 36"><circle cx="18" cy="18" r="17" fill="#8cc63f"/><path d="M18 27V14M18 18c-4 0-6-3-6-6 4 0 6 3 6 6zM18 16c4 0 6-3 6-6-4 0-6 3-6 6z" stroke="#fff" stroke-width="1.4" fill="none"/></svg>
      <h3>Versatility with<br>contract growing</h3>
    </div>
    <p>Need a specialised turf solution tailored to your unique specifications? Our contract growing services ensure that you get precisely what you order. We work closely with our clients, offering customized growing solutions to meet specific requirements, ensuring a seamless integration with your landscaping plans.</p>
  </article>

  <article class="feature" style="left:274px;top:486px;width:235px">
    <div class="feature__head">
      <svg class="badge" viewBox="0 0 36 36"><circle cx="18" cy="18" r="17" fill="#8cc63f"/><circle cx="18" cy="19" r="6" stroke="#fff" stroke-width="1.4" fill="none"/><path d="M15 19l2 2 4-4" stroke="#fff" stroke-width="1.4" fill="none"/></svg>
      <h3>Unmatched quality<br>and expertise</h3>
    </div>
    <p>At Meridell Turf Solutions, we don't just provide turf – we deliver a promise of quality, resilience, and expertise. Our team is dedicated to ensuring your satisfaction, from the initial consultation to the delivery of the perfect turf for your space <span class="cta">contact us today and experience the Meridell Advantage!</span></p>
  </article>

  <article class="feature" style="left:32px;top:515px;width:220px">
    <div class="feature__head">
      <svg class="badge" viewBox="0 0 36 36"><circle cx="18" cy="18" r="17" fill="#8cc63f"/><path d="M13 26V15l5-5 5 5v11z" stroke="#fff" stroke-width="1.4" fill="none"/></svg>
      <h3>Dedication to<br>excellence</h3>
    </div>
    <p>At Meridell Turf Solutions, we are dedicated to providing the highest standard of turf for a wide range of applications. Our commitment goes beyond delivering turf – it's about transforming spaces into green havens that stand the test of time.</p>
  </article>

  <div class="footer-contact">
    <span class="label">CONTACT US</span>
    <span class="contact-item" style="left:149px"><svg viewBox="0 0 10 10"><path d="M2 1l2 2-1 1.5c.8 1.5 1.5 2.2 3 3L7.5 6.5l2 2-1.5 1.5C4 9.5.5 6 0 2.5z" fill="none" stroke="#7bbaa8" stroke-width=".9"/></svg>0400 317 262</span>
    <span class="contact-item" style="left:235px"><svg viewBox="0 0 10 10"><rect x=".5" y="2" width="9" height="6" fill="none" stroke="#7bbaa8" stroke-width=".9"/><path d="M.5 2l4.5 3.5L9.5 2" fill="none" stroke="#7bbaa8" stroke-width=".9"/></svg>turf@meridellgroup.com.au</span>
    <span class="contact-item" style="left:388px"><svg viewBox="0 0 10 10"><circle cx="5" cy="5" r="4.4" fill="none" stroke="#7bbaa8" stroke-width=".9"/><path d="M.6 5h8.8M5 .6c-2.5 3-2.5 5.8 0 8.8M5 .6c2.5 3 2.5 5.8 0 8.8" fill="none" stroke="#7bbaa8" stroke-width=".8"/></svg>meridellgroup.com.au</span>
  </div>
</section>

<!-- ===== Back page ===== -->
<section class="page page--back">
  <svg class="backdrop" viewBox="0 0 521 673">
    <defs>
      <linearGradient id="varietyPanel" x1="0" y1="1" x2="1" y2="0">
        <stop offset="0" stop-color="#17507a"/>
        <stop offset="0.5" stop-color="#1d6274"/>
        <stop offset="1" stop-color="#8cc63f"/>
      </linearGradient>
      <linearGradient id="ringGreen2" x1="0" y1="0" x2="1" y2="1">
        <stop offset="0" stop-color="#8cc63f"/>
        <stop offset="1" stop-color="#2f7a5a"/>
      </linearGradient>
      <linearGradient id="aerialPhoto" x1="0" y1="0" x2="0" y2="1">
        <stop offset="0" stop-color="#9fc3e6"/>
        <stop offset="0.2" stop-color="#5d7b4a"/>
        <stop offset="0.6" stop-color="#8aa14a"/>
        <stop offset="1" stop-color="#6d8f36"/>
      </linearGradient>
      <linearGradient id="grassTop" x1="0" y1="0" x2="0" y2="1">
        <stop offset="0" stop-color="#9ad35a"/>
        <stop offset="0.75" stop-color="#4b9a32"/>
        <stop offset="1" stop-color="#3b2e25"/>
      </linearGradient>
      <linearGradient id="lawnPhoto2" x1="0" y1="0" x2="0" y2="1">
        <stop offset="0" stop-color="#9cc0d8"/>
        <stop offset="0.35" stop-color="#5b8a48"/>
        <stop offset="1" stop-color="#5fa43a"/>
      </linearGradient>
    </defs>
    <path d="M0,80 C200,88 380,52 521,0 L521,350 C430,372 320,378 240,378 L200,440 C120,470 40,470 0,455 Z" fill="url(#varietyPanel)"/>
    <path d="M320,385 C400,382 470,372 521,355 L521,362 C470,380 400,388 320,388 Z" fill="#8cc63f"/>
    <path d="M220,12 C320,18 440,5 521,2 L521,40 C470,60 420,80 360,88 L240,88 Z" fill="url(#grassTop)" role="img" aria-label="Image: tall turf grass blades with soil layer"/>
    <circle cx="108" cy="306" r="151" fill="#17507a"/>
    <circle cx="106" cy="304" r="143" fill="url(#ringGreen2)"/>
    <circle cx="104" cy="308" r="136" fill="url(#aerialPhoto)" role="img" aria-label="Photo: aerial view of turf farm fields lined with trees"/>
    <path d="M0,673 L0,615 C150,598 360,612 521,588 L521,673 Z" fill="#17507a"/>
    <path d="M150,608 C280,600 400,606 521,584 L521,590 C400,612 280,606 150,611 Z" fill="#8cc63f"/>
    <circle cx="80" cy="712" r="110" fill="#7bbaa8"/>
    <circle cx="76" cy="714" r="103" fill="url(#lawnPhoto2)" role="img" aria-label="Photo: green lawn in front of a building"/>
  </svg>

  <div class="brand" style="left:33px;top:22px">
    <span class="brand__dot"></span>
    <span class="brand__name">MERIDELL<br>TURF SOLUTIONS</span>
  </div>

  <div class="abs varieties-pill">Turf Varieties grown and available</div>

  <div class="variety" style="left:142px;top:126px;width:345px">
    <h4><svg viewBox="0 0 12 12"><circle cx="6" cy="6" r="5.6" fill="#fff"/><path d="M3.5 6l1.8 1.8 3.3-3.6" stroke="#17507a" stroke-width="1.3" fill="none"/></svg>SANTA ANNA COUCH</h4>
    <p style="padding-left:17px">Known for its resilience and fine texture, Santa Anna Couch is a versatile turf variety ideal for creating lush, green landscapes that can withstand various environmental conditions.</p>
  </div>
  <div class="variety" style="left:198px;top:172px;width:290px">
    <h4><svg viewBox="0 0 12 12"><circle cx="6" cy="6" r="5.6" fill="#fff"/><path d="M3.5 6l1.8 1.8 3.3-3.6" stroke="#17507a" stroke-width="1.3" fill="none"/></svg>WINTERGREEN COUCH</h4>
    <p style="padding-left:17px">Wintergreen Couch is prized for its vibrant green colour and dense growth, making it a popular choice for lawns and sports fields, providing a soft and inviting surface.</p>
  </div>
  <div class="variety" style="left:237px;top:228px;width:252px">
    <h4><svg viewBox="0 0 12 12"><circle cx="6" cy="6" r="5.6" fill="#fff"/><path d="M3.5 6l1.8 1.8 3.3-3.6" stroke="#17507a" stroke-width="1.3" fill="none"/></svg>KIKUYU</h4>
    <p style="padding-left:17px">Renowned for its rapid growth, durability, and ability to thrive in various climates, Kikuyu turf is a popular choice for lawns, sports fields, and recreational areas, providing a resilient and vibrant green surface.</p>
  </div>
  <div class="variety" style="left:249px;top:296px;width:252px">
    <h4><svg viewBox="0 0 12 12"><circle cx="6" cy="6" r="5.6" fill="#fff"/><path d="M3.5 6l1.8 1.8 3.3-3.6" stroke="#17507a" stroke-width="1.3" fill="none"/></svg>OVERSOWN RYE GRASS BLENDS<br>(OVERSOWN TO ORDER):</h4>
    <p style="padding-left:17px">Our Oversown Rye Grass Blends are tailored to order, offering a flexible solution for enhancing turf durability and maintaining a lush appearance, especially during colder seasons.</p>
  </div>

  <h2 class="abs testimonials-title">Testimonials</h2>
  <div class="testimonial" style="top:425px"><span class="quote">“</span><p>Lorem Ipsum is simply dummy text of the printing and typesetting industry. Lorem Ipsum has been the industry's standard dummy text ever since the 1500s,</p><span class="author">- Lorem duumy</span></div>
  <div class="testimonial" style="top:485px"><span class="quote">“</span><p>Lorem Ipsum is simply dummy text of the printing and typesetting industry. Lorem Ipsum has been the industry's standard dummy text ever since the 1500s,</p><span class="author">- Lorem duumy</span></div>
  <div class="testimonial" style="top:545px"><span class="quote">“</span><p>Lorem Ipsum is simply dummy text of the printing and typesetting industry. Lorem Ipsum has been the industry's standard dummy text ever since the 1500s,</p><span class="author">- Lorem duumy</span></div>

  <h2 class="abs services-title">Meridell <span class="accent">Turf Solutions</span><br>Services:</h2>
  <ul class="abs services-list">
    <li><svg viewBox="0 0 10 10"><circle cx="5" cy="5" r="4.8" fill="#8cc63f"/><path d="M3 5l1.4 1.4L7 3.8" stroke="#fff" stroke-width="1.1" fill="none"/></svg>Turf supply</li>
    <li><svg viewBox="0 0 10 10"><circle cx="5" cy="5" r="4.8" fill="#8cc63f"/><path d="M3 5l1.4 1.4L7 3.8" stroke="#fff" stroke-width="1.1" fill="none"/></svg>Domestic &amp; commercial sales</li>
    <li><svg viewBox="0 0 10 10"><circle cx="5" cy="5" r="4.8" fill="#8cc63f"/><path d="M3 5l1.4 1.4L7 3.8" stroke="#fff" stroke-width="1.1" fill="none"/></svg>Thick cut turf, supplied in either maxi rolls or standard turf rolls</li>
    <li><svg viewBox="0 0 10 10"><circle cx="5" cy="5" r="4.8" fill="#8cc63f"/><path d="M3 5l1.4 1.4L7 3.8" stroke="#fff" stroke-width="1.1" fill="none"/></svg>Contract growing</li>
    <li><svg viewBox="0 0 10 10"><circle cx="5" cy="5" r="4.8" fill="#8cc63f"/><path d="M3 5l1.4 1.4L7 3.8" stroke="#fff" stroke-width="1.1" fill="none"/></svg>Pick up or delivery</li>
  </ul>

  <div class="footer-contact">
    <span class="label">CONTACT US</span>
    <span class="contact-item" style="left:149px"><svg viewBox="0 0 10 10"><path d="M2 1l2 2-1 1.5c.8 1.5 1.5 2.2 3 3L7.5 6.5l2 2-1.5 1.5C4 9.5.5 6 0 2.5z" fill="none" stroke="#7bbaa8" stroke-width=".9"/></svg>0400 317 262</span>
    <span class="contact-item" style="left:235px"><svg viewBox="0 0 10 10"><rect x=".5" y="2" width="9" height="6" fill="none" stroke="#7bbaa8" stroke-width=".9"/><path d="M.5 2l4.5 3.5L9.5 2" fill="none" stroke="#7bbaa8" stroke-width=".9"/></svg>turf@meridellgroup.com.au</span>
    <span class="contact-item" style="left:388px"><svg viewBox="0 0 10 10"><circle cx="5" cy="5" r="4.4" fill="none" stroke="#7bbaa8" stroke-width=".9"/><path d="M.6 5h8.8M5 .6c-2.5 3-2.5 5.8 0 8.8M5 .6c2.5 3 2.5 5.8 0 8.8" fill="none" stroke="#7bbaa8" stroke-width=".8"/></svg>meridellgroup.com.au</span>
  </div>
</section>

</body>
</html>
```